The name of my company is Tolmen Refacing LLC and I would like the sub text to say "Cabinet Refacing and Countertops". Have my name Dorian Tolmen, Owner / Sales, contact info: Cell: 360-555-0147 / Email: dorian.tolmen@quenmail.com

Simple, Clean, and Organized. With colors that will appeal to the eye.

Target Market(s)

Houses and Apartments

Industry/Entity Type

Cabinet Refacing

Contact Information for Business Card

Company name and sub text Dorian Tolmen - Owner / Sales, my cell phone number and email

Requirements
Must have
• Business name, my name / position, and my contact info
Nice to have
• Simple. Organized. Appealing to the eye

```html
<!DOCTYPE html>
<html lang="en">
<head>
<meta charset="utf-8">
<title>Tolmen Refacing LLC – Business Cards</title>
<link rel="stylesheet" href="https://fonts.googleapis.com/css2?family=Montserrat:wght@300;400;500;600&display=swap">
<style>
  :root {
    --backdrop: #1c1c1e;
    --card: #0b0b0c;
    --brand-blue: #4a72c4;
    --text-grey: #b9b9bc;
    --text-light: #e4e4e6;
    --divider: #4a4a4e;
  }
  * { box-sizing: border-box; margin: 0; padding: 0; }
  html, body {
    width: 1200px; height: 900px; overflow: hidden;
    background: var(--backdrop);
    font-family: "Montserrat", Arial, sans-serif;
  }
  .canvas {
    width: 1200px; height: 900px;
    display: flex; align-items: center; justify-content: center; gap: 60px;
  }
  .card {
    width: 525px; height: 300px;
    background: var(--card);
    border-radius: 3px;
    box-shadow: 0 14px 40px rgba(0,0,0,.55);
    position: relative;
  }
  /* Contact side */
  .card--contact { display: flex; align-items: center; }
  .brand-block {
    width: 265px; height: 100%;
    display: flex; align-items: center; justify-content: center; gap: 10px;
  }
  .brand-mark {
    width: 14px; height: 14px; background: var(--brand-blue); flex: none;
  }
  .brand-name {
    font-weight: 300; font-size: 17px; letter-spacing: .06em;
    color: var(--text-grey); white-space: nowrap;
  }
  .column-divider {
    width: 1px; height: 120px; background: var(--divider);
  }
  .contact-block { padding-left: 26px; }
  .person-name {
    font-weight: 600; font-size: 19px; letter-spacing: .02em;
    color: var(--brand-blue); line-height: 1.1;
  }
  .person-role {
    font-weight: 400; font-size: 13px; color: var(--text-grey);
    margin-top: 2px;
  }
  .contact-list { list-style: none; margin-top: 26px; }
  .contact-item {
    display: flex; align-items: center; gap: 8px;
    font-weight: 400; font-size: 12.5px; color: var(--text-grey);
    line-height: 1.7;
  }
  .contact-icon { width: 13px; height: 13px; flex: none; }
  /* Front side */
  .card--front {
    display: flex; flex-direction: column; align-items: center; justify-content: center;
    text-align: center;
  }
  .front-brand { display: flex; align-items: center; gap: 12px; }
  .front-brand .brand-mark { width: 18px; height: 18px; }
  .front-brand .brand-name { font-size: 27px; }
  .front-tagline {
    margin-top: 10px; font-weight: 500; font-size: 15px;
    color: var(--text-light); letter-spacing: .01em;
  }
</style>
</head>
<body>
<main class="canvas">
  <section class="card card--contact">
    <div class="brand-block">
      <span class="brand-mark"></span>
      <span class="brand-name">TOLMEN REFACING, LLC</span>
    </div>
    <div class="column-divider"></div>
    <div class="contact-block">
      <h1 class="person-name">DORIAN TOLMEN</h1>
      <p class="person-role">Owner / Sales</p>
      <ul class="contact-list">
        <li class="contact-item">
          <svg class="contact-icon" viewBox="0 0 24 24" aria-hidden="true">
            <path fill="var(--brand-blue)" d="M6.6 10.8a15.2 15.2 0 0 0 6.6 6.6l2.2-2.2a1 1 0 0 1 1-.25 11.4 11.4 0 0 0 3.6.57 1 1 0 0 1 1 1V20a1 1 0 0 1-1 1A17 17 0 0 1 3 4a1 1 0 0 1 1-1h3.5a1 1 0 0 1 1 1c0 1.25.2 2.45.57 3.57a1 1 0 0 1-.25 1z"/>
          </svg>
          360-555-0147
        </li>
        <li class="contact-item">
          <svg class="contact-icon" viewBox="0 0 24 24" aria-hidden="true">
            <rect x="2" y="5" width="20" height="14" fill="var(--brand-blue)"/>
            <path d="M2 5l10 8 10-8" fill="none" stroke="var(--card)" stroke-width="1.6"/>
          </svg>
          dorian.tolmen@quenmail.com
        </li>
      </ul>
    </div>
  </section>

  <section class="card card--front">
    <div class="front-brand">
      <span class="brand-mark"></span>
      <span class="brand-name">TOLMEN REFACING, LLC</span>
    </div>
    <p class="front-tagline">Cabinet Refacing and Countertops</p>
  </section>
</main>
</body>
</html>
```